Stationery Design Project - Mark Delouris

I have recently designed my personal logo - Mark Delouris (here on briefhivo.net) and now i'm looking to complete my corporate identity, with adding:
- Business Card
- Letter Head
- Envelope
- Brochure template (that will be used to promote any of the workshops or other services I provide along with a short summary about my credentials, and testimonials) - you can take your pick from the website: http://markdelouris.net

Refer to website for more insight into the brand and the look & feel

PS.
- PLEASE REFER TO ATTACHED FILE AND READ THE "SHOULD NOT HAVE SECTION OF THIS BRIEF"
- I have attached two vector files, displaying the logo alteration on two different backgrounds (dark & light)

ONLY 2 DAYS LEFT ON DEADLINE. KEEP THOSE DESIGNS COMING.

Target Market(s)

1) One-on-one Business Executive 2) Companies requesting my workshops for mid management teams & public speaking events like KIP Forums

Industry/Entity Type

Business

Requirements
Must have
• - must fit the look and feel of the logo (notice that I have attached the logo, and an emblem)
- the final files should be ready for printing - with info on colours, sizes, bleed area, margins, UV spot (if applicable), suggested material to print on (applies to business cards in particular)
- brand guide lines should be laid out too (font, colour, etc ...)
Nice to have
• It would be nice to produce something different that your standard sizes & di-cut in terms of business card, and letter head ...
Should not have
• THE EMBLEM (MD) AND THE LOGO (MARK DELOURIS) SHOULD NOT BE LAYED OUT AS PER THE ATTACHED FILE - THEY SHOULD BE SEPARATED - THE EMBLEM (MD) CAN BE USED IN PARTIAL OR AS WATERMARK - BUT NOT THE LOGO (MARK DELOURIS)

```html
<!DOCTYPE html>
<html lang="en">
<head>
<meta charset="utf-8">
<title>Mark Delouris – Stationery Set</title>
<link rel="stylesheet" href="https://fonts.googleapis.com/css2?family=Oswald:wght@600&family=Open+Sans:wght@400;600&family=Noto+Serif:wght@400&display=swap">
<style>
  :root {
    --sky: #6ec1ee;
    --charcoal: #5d5a5b;
    --ink: #3b3a3b;
    --text: #5a5a5a;
    --paper: #ffffff;
    --backdrop: #e8e9eb;
    --mark-faint: #eceef0;
    --metal-dark: #8d8e91;
    --metal-light: #cbccce;
  }
  * { margin: 0; padding: 0; box-sizing: border-box; }
  html, body { width: 1200px; height: 888px; overflow: hidden; }
  body {
    background: var(--backdrop);
    font-family: "Open Sans", Arial, sans-serif;
    color: var(--text);
    position: relative;
  }
  .sheet { position: absolute; background: var(--paper); overflow: hidden; box-shadow: 0 2px 6px rgba(0,0,0,.12); }

  .wordmark {
    font-family: "Oswald", "Arial Narrow", sans-serif;
    font-weight: 600;
    color: var(--ink);
    letter-spacing: .02em;
    line-height: 1;
    white-space: nowrap;
  }
  .watermark { position: absolute; border-radius: 50%; border: 10px solid var(--mark-faint); }

  .contact-list { list-style: none; }
  .contact-list li { display: flex; align-items: center; gap: 4px; white-space: nowrap; }
  .contact-list svg { flex: none; }

  /* Letterhead */
  .letterhead { left: 40px; top: 40px; width: 320px; height: 452px; }
  .letterhead .site-url { position: absolute; left: 24px; top: 20px; font-size: 7px; }
  .letterhead .wordmark { position: absolute; right: 24px; top: 46px; font-size: 17px; }
  .letterhead .watermark { left: 100px; top: 150px; width: 120px; height: 120px; }
  .letterhead .contact-list { position: absolute; left: 24px; top: 380px; font-size: 6px; line-height: 10px; }
  .letterhead .footer-band { position: absolute; left: 0; bottom: 0; }

  /* Business cards */
  .card { width: 280px; height: 160px; left: 60px; }
  .card-front { top: 520px; }
  .card-front .wordmark { position: absolute; left: 18px; top: 30px; font-size: 15px; }
  .card-front .person { position: absolute; left: 150px; top: 26px; }
  .card-front .person-name { color: var(--sky); font-size: 12px; font-weight: 600; }
  .card-front .person-role { font-size: 8px; margin-top: 1px; }
  .card-front .contact-list { position: absolute; left: 150px; top: 70px; font-size: 7px; line-height: 13px; }
  .card-front .edge { position: absolute; left: 0; bottom: 0; width: 100%; height: 5px; background: var(--sky); }
  .card-back { top: 700px; background: var(--charcoal); }
  .card-back .emblem { position: absolute; left: 116px; top: 34px; width: 48px; height: 48px; border-radius: 50%; background: var(--paper); }
  .card-back .site-url { position: absolute; left: 0; width: 100%; top: 94px; text-align: center; color: var(--paper); font-size: 8px; }

  /* Brochure */
  .brochure { left: 470px; top: 70px; width: 620px; height: 438px; display: flex; }
  .brochure-spine { width: 110px; position: relative; border-right: 4px solid var(--sky); }
  .brochure-spine .wordmark { position: absolute; left: 34px; bottom: 28px; font-size: 26px; transform: rotate(-90deg); transform-origin: left bottom; translate: 26px 0; }
  .brochure-spine .site-url { position: absolute; left: 70px; top: 22px; font-size: 9px; writing-mode: vertical-rl; font-weight: 600; color: var(--ink); }
  .brochure-body {
    width: 436px; position: relative;
    background: linear-gradient(100deg, var(--metal-dark) 0%, var(--metal-light) 45%, #a7a8ab 70%, var(--metal-dark) 100%);
  }
  .brochure-photo {
    position: absolute; right: 0; top: 0; width: 250px; height: 200px;
    background: linear-gradient(135deg, #9c9c9e 0%, #6b6b6d 55%, #3e3e40 100%);
  }
  .brochure-quote { position: absolute; left: 40px; top: 236px; font-family: "Noto Serif", Georgia, serif; color: var(--paper); font-size: 26px; white-space: nowrap; }
  .brochure-quote cite { display: block; text-align: right; font-family: "Open Sans", Arial, sans-serif; font-style: normal; font-size: 8px; margin-top: 4px; color: #f2f2f2; }
  .brochure-emblem { position: absolute; right: 8px; top: 8px; width: 40px; height: 40px; border-radius: 50%; background: var(--paper); border: 3px solid var(--ink); }
  .brochure-rail { width: 70px; background: var(--sky); position: relative; }
  .brochure-rail .contact-list { position: absolute; left: 22px; bottom: 24px; writing-mode: vertical-rl; transform: rotate(180deg); font-size: 8px; line-height: 13px; color: var(--ink); }
  .brochure-rail .contact-list li { flex-direction: row; }

  /* Envelopes */
  .envelope { top: 560px; width: 370px; height: 185px; }
  .envelope-front { left: 400px; }
  .envelope-front .wordmark { position: absolute; left: 22px; top: 22px; font-size: 17px; }
  .envelope-front .contact-list { position: absolute; left: 22px; top: 92px; font-size: 6.5px; line-height: 11px; }
  .envelope-front .watermark { left: 232px; top: 66px; width: 96px; height: 96px; border-width: 8px; }
  .envelope-front .footer-band { position: absolute; left: 0; bottom: 0; }
  .envelope-back { left: 790px; }
  .envelope-back .flap { position: absolute; left: 0; top: 0; }
  .envelope-back .emblem { position: absolute; left: 164px; top: 20px; width: 42px; height: 42px; border-radius: 50%; background: var(--paper); }
</style>
</head>
<body>

  <section class="sheet letterhead" aria-label="Letterhead">
    <p class="site-url">www.markdelouris.net</p>
    <p class="wordmark">MARK DELOURIS</p>
    <div class="watermark"></div>
    <ul class="contact-list">
      <li><svg width="7" height="7" viewBox="0 0 10 10"><rect width="10" height="10" fill="#5d5a5b"/><path d="M5 2a2 2 0 0 1 2 2c0 1.5-2 4-2 4S3 5.5 3 4a2 2 0 0 1 2-2z" fill="#fff"/></svg>Larnessa - Veloria, P.O.Box 41-286 Corvane</li>
      <li><svg width="7" height="7" viewBox="0 0 10 10"><rect width="10" height="10" fill="#5d5a5b"/><path d="M3 2h1.5l.6 1.8-1 .7a4 4 0 0 0 1.6 1.6l.7-1 1.8.6V7.5A.7.7 0 0 1 7.5 8 5.5 5.5 0 0 1 2 2.5.7.7 0 0 1 3 2z" fill="#fff"/></svg>00412 55 318207</li>
      <li><svg width="7" height="7" viewBox="0 0 10 10"><rect width="10" height="10" fill="#5d5a5b"/><path d="M2 3h6v4H2z" fill="#fff"/><path d="M2 3l3 2.2L8 3" stroke="#5d5a5b" stroke-width=".8" fill="none"/></svg>me@markdelouris.net</li>
    </ul>
    <svg class="footer-band" width="320" height="30" viewBox="0 0 320 30">
      <polygon points="0,6 320,18 320,22 0,10" fill="var(--sky)"/>
      <polygon points="210,14 320,19 320,30 200,30" fill="var(--charcoal)"/>
    </svg>
  </section>

  <section class="sheet card card-front" aria-label="Business card front">
    <p class="wordmark">MARK DELOURIS</p>
    <div class="person">
      <p class="person-name">Mark Delouris</p>
      <p class="person-role">Consultant</p>
    </div>
    <ul class="contact-list">
      <li>P.O.Box 41-286 Corvane</li>
      <li>00412 55 318207</li>
      <li>me@markdelouris.net</li>
      <li>www.markdelouris.net</li>
    </ul>
    <div class="edge"></div>
  </section>

  <section class="sheet card card-back" aria-label="Business card back">
    <div class="emblem"></div>
    <p class="site-url">www.markdelouris.net</p>
  </section>

  <section class="sheet brochure" aria-label="Brochure">
    <div class="brochure-spine">
      <p class="site-url">www.markdelouris.net</p>
      <p class="wordmark">MARK DELOURIS</p>
    </div>
    <div class="brochure-body">
      <div class="brochure-photo" role="img" aria-label="Portrait photograph of Mark Delouris in a dark suit"></div>
      <div class="brochure-emblem"></div>
      <blockquote class="brochure-quote">“You Wait ... You Fade!”<cite>Mark Delouris</cite></blockquote>
    </div>
    <div class="brochure-rail">
      <ul class="contact-list">
        <li>Larnessa - Veloria, P.O.Box 41-286 Corvane</li>
        <li>00412 55 318207</li>
        <li>me@markdelouris.net</li>
      </ul>
    </div>
  </section>

  <section class="sheet envelope envelope-front" aria-label="Envelope front">
    <p class="wordmark">MARK DELOURIS</p>
    <ul class="contact-list">
      <li><svg width="7" height="7" viewBox="0 0 10 10"><rect width="10" height="10" fill="#5d5a5b"/><path d="M5 2a2 2 0 0 1 2 2c0 1.5-2 4-2 4S3 5.5 3 4a2 2 0 0 1 2-2z" fill="#fff"/></svg>Larnessa - Veloria, P.O.Box 41-286 Corvane</li>
      <li><svg width="7" height="7" viewBox="0 0 10 10"><rect width="10" height="10" fill="#5d5a5b"/><path d="M3 2h1.5l.6 1.8-1 .7a4 4 0 0 0 1.6 1.6l.7-1 1.8.6V7.5A.7.7 0 0 1 7.5 8 5.5 5.5 0 0 1 2 2.5.7.7 0 0 1 3 2z" fill="#fff"/></svg>00412 55 318207 <svg width="7" height="7" viewBox="0 0 10 10"><rect width="10" height="10" fill="#5d5a5b"/><path d="M2 3h6v4H2z" fill="#fff"/><path d="M2 3l3 2.2L8 3" stroke="#5d5a5b" stroke-width=".8" fill="none"/></svg>me@markdelouris.net</li>
    </ul>
    <div class="watermark"></div>
    <svg class="footer-band" width="370" height="34" viewBox="0 0 370 34">
      <polygon points="0,4 370,18 370,22 0,8" fill="var(--sky)"/>
      <polygon points="230,13 370,19 370,34 220,34" fill="var(--charcoal)"/>
    </svg>
  </section>

  <section class="sheet envelope envelope-back" aria-label="Envelope back">
    <svg class="flap" width="370" height="84" viewBox="0 0 370 84">
      <polygon points="0,0 370,0 370,84 0,56" fill="var(--charcoal)"/>
    </svg>
    <div class="emblem"></div>
  </section>

</body>
</html>
```